Marlowe Holdings LLC - Business Cards

Need the following information on the cards:

Name: Dean R Vossler
Title: Chief Executive Manager

Business address:
412 N Ridgeview Lane #118
Glen Harbor, Il 60412

Phone: (630) 555-0148 - Business
KPV FFL license number: 5-21-xxx-xx-xx-04519
Email: dean.vossler@marloweholdingsffl.com

Target Market(s)

Firearm owners

Industry/Entity Type

Firearms industry,

Contact Information for Business Card

Contact number, name and title, web page address, email, business address and kpv license number,

Requirements
Must have
• Name, title, business address, phone numbers, KPV license numbers, web page address and email address.
Nice to have
• Cellphone number,

```html
<!DOCTYPE html>
<html lang="en">
<head>
<meta charset="utf-8">
<title>Marlowe Holdings LLC – Business Cards</title>
<link rel="stylesheet" href="https://fonts.googleapis.com/css2?family=Montserrat:wght@400;600;700&display=swap">
<style>
  :root{
    --paper:#ffffff;
    --ink:#1b1b1d;
    --panel:#1d1e20;
    --red-bright:#e8141e;
    --red:#c80f14;
    --red-mid:#a50d0d;
    --red-deep:#7a0a0a;
    --red-wine:#650a12;
    --text-light:#ffffff;
  }
  *{margin:0;padding:0;box-sizing:border-box;}
  html,body{width:1200px;height:360px;overflow:hidden;background:var(--paper);}
  body{position:relative;font-family:"Montserrat",Arial,sans-serif;}
  .card{position:absolute;top:0;height:358px;width:594px;overflow:hidden;}
  .card-front{left:0;background:var(--paper);}
  .card-back{left:606px;background:var(--panel);}
  .card-shapes{position:absolute;inset:0;}
  .brand{position:absolute;display:flex;flex-direction:column;align-items:center;justify-content:center;text-align:center;
         color:var(--red);font-weight:700;text-transform:uppercase;letter-spacing:1px;line-height:1.15;}
  .brand-ring{position:absolute;border-radius:50%;}
  .brand-front{left:22px;top:11px;width:136px;height:136px;font-size:14px;}
  .brand-front .brand-ring{inset:0;border:2px solid var(--ink);}
  .brand-back{left:285px;top:100px;width:158px;height:158px;font-size:17px;}
  .brand-back .brand-ring{inset:0;border:2px solid var(--text-light);}
  .person{position:absolute;left:341px;top:50px;}
  .person-name{font-size:16px;font-weight:700;color:var(--ink);letter-spacing:.6px;text-transform:uppercase;}
  .person-title{margin-top:7px;font-size:12px;font-weight:700;color:var(--red);}
  .contact{position:absolute;left:291px;list-style:none;color:var(--text-light);font-size:12.5px;letter-spacing:.5px;line-height:17px;}
  .contact li{position:absolute;left:0;display:flex;align-items:flex-start;white-space:nowrap;}
  .contact .icon{width:24px;height:24px;margin-right:27px;flex:none;}
  .contact-phone{top:188px;}
  .contact-email{top:222px;}
  .contact-address{top:264px;}
  .contact-address .icon{margin-right:20px;}
  .license{position:absolute;left:199px;top:304px;color:var(--text-light);font-size:12.5px;letter-spacing:.9px;}
</style>
</head>
<body>

<section class="card card-front">
  <svg class="card-shapes" width="594" height="358" viewBox="0 0 594 358">
    <rect x="204" y="148" width="390" height="210" fill="var(--panel)"/>
    <rect x="110" y="211" width="15" height="147" fill="var(--red-deep)"/>
    <rect x="131" y="211" width="16" height="147" fill="var(--red)"/>
    <rect x="139" y="172" width="35" height="186" fill="var(--red-deep)"/>
    <rect x="174" y="119" width="30" height="239" fill="var(--red-mid)"/>
    <rect x="213" y="119" width="15" height="172" fill="var(--red-bright)"/>
  </svg>

  <div class="brand brand-front"><span class="brand-ring"></span>Marlowe<br>Holdings LLC</div>

  <div class="person">
    <h1 class="person-name">Dean R Vossler</h1>
    <p class="person-title">Chief Executive Manager</p>
  </div>

  <ul class="contact">
    <li class="contact-phone">
      <svg class="icon" viewBox="0 0 24 24"><path fill="#fff" d="M6.6 3.2c.6-.5 1.4-.4 1.8.2l2 3c.4.6.3 1.3-.2 1.8L9 9.4c.9 2 2.6 3.8 4.6 4.7l1.2-1.2c.5-.5 1.2-.6 1.8-.2l3 2c.6.4.7 1.2.2 1.8l-1.6 1.8c-.8.9-2.1 1.2-3.2.8C9.7 17.3 6.7 14.3 5 9.1c-.4-1.1-.1-2.4.8-3.2z"/></svg>
      <span>630-555-0148</span>
    </li>
    <li class="contact-email">
      <svg class="icon" viewBox="0 0 24 24"><rect x="1" y="5" width="22" height="15" fill="#fff"/><path d="M1.5 5.5 12 13.5 22.5 5.5" fill="none" stroke="var(--panel)" stroke-width="1.6"/></svg>
      <span>dean.vossler<br>@marloweholdingsffl.com</span>
    </li>
    <li class="contact-address">
      <svg class="icon" viewBox="0 0 24 24"><path fill="#fff" d="M12 1.5c-4.2 0-7.5 3.3-7.5 7.4 0 5.4 7.5 13.6 7.5 13.6s7.5-8.2 7.5-13.6c0-4.1-3.3-7.4-7.5-7.4zm0 10.3a2.9 2.9 0 1 1 0-5.8 2.9 2.9 0 0 1 0 5.8z"/></svg>
      <span>412 N Ridgeview Lane #118<br>Glen Harbor, Il 60412</span>
    </li>
  </ul>
</section>

<section class="card card-back">
  <svg class="card-shapes" width="594" height="358" viewBox="0 0 594 358">
    <rect x="39" y="161" width="21" height="197" fill="var(--red-deep)"/>
    <rect x="69" y="161" width="21" height="197" fill="var(--red-mid)"/>
    <rect x="79" y="110" width="46" height="248" fill="var(--red-wine)"/>
    <rect x="125" y="0" width="39" height="358" fill="var(--red-mid)"/>
    <rect x="176" y="0" width="20" height="246" fill="var(--red-bright)"/>
  </svg>

  <div class="brand brand-back"><span class="brand-ring"></span>Marlowe<br>Holdings LLC</div>

  <p class="license">KPV FFL license number: 5-21-xxx-xx-xx-04519</p>
</section>

</body>
</html>
```